Simple Business Card Design

Professional/clean business card with custom logo included in layout.

Target Market(s)

N/A

Industry/Entity Type

Business

Contact Information for Business Card

Name: Marlene Voskin, PT; NV Medicaid Provider; Phone: (775) 918-2246; Toll-free phone: (877) 461-5092; email: mar@tidewellbranchsystemsltd.example

Font styles to use
Serif
Decorative
Script

Requirements
Must have
• See "details" above.
Nice to have
• Would be interested to see dark vs. light/grayscale backgrounds that accentuate/contrast the logo colors. (I.e. dark navy background w/ white or grey text, etc.)

```html
<!DOCTYPE html>
<html lang="en">
<head>
<meta charset="utf-8">
<title>Tidewell Branch Systems Ltd. – Business Card</title>
<link href="https://fonts.googleapis.com/css2?family=Dancing+Script:wght@700&family=Josefin+Sans:wght@300;400&display=swap" rel="stylesheet">
<style>
  :root {
    --page-bg: #e9e6e1;
    --card-blue: #3553a9;
    --card-blue-light: #4764b8;
    --ink-white: #ffffff;
    --ink-soft: #d9def0;
    --rule: #c9d0e8;
  }
  * { margin: 0; padding: 0; box-sizing: border-box; }
  html, body {
    width: 1200px;
    height: 900px;
    overflow: hidden;
    background: var(--page-bg);
  }
  .card {
    position: absolute;
    left: 100px;
    top: 164px;
    width: 1000px;
    height: 572px;
    background: linear-gradient(135deg, var(--card-blue-light) 0%, var(--card-blue) 55%);
    color: var(--ink-white);
    font-family: "Josefin Sans", sans-serif;
    box-shadow: 0 10px 30px rgba(0,0,0,0.18);
  }
  .brand {
    position: absolute;
    left: 50px;
    top: 236px;
    width: 260px;
    display: flex;
    align-items: center;
    gap: 12px;
  }
  .brand-dot {
    flex: none;
    width: 34px;
    height: 34px;
    border-radius: 50%;
    background: var(--ink-white);
  }
  .brand-name {
    font-weight: 400;
    font-size: 21px;
    line-height: 1.25;
    letter-spacing: 1px;
    text-transform: uppercase;
    color: var(--ink-white);
  }
  .rule {
    position: absolute;
    height: 2px;
    background: var(--rule);
  }
  .rule-top { left: 380px; right: 40px; top: 150px; }
  .rule-bottom { left: 320px; right: 40px; top: 452px; }
  .contact {
    position: absolute;
    left: 380px;
    top: 186px;
  }
  .contact-name {
    font-family: "Dancing Script", cursive;
    font-weight: 700;
    font-size: 46px;
    line-height: 1;
    margin-bottom: 26px;
  }
  .contact-role {
    font-weight: 300;
    font-size: 25px;
    color: var(--ink-soft);
    margin-bottom: 32px;
    word-spacing: 4px;
  }
  .contact-line {
    font-weight: 400;
    font-size: 24px;
    line-height: 1.2;
    margin-bottom: 20px;
  }
  .contact-line .gap { display: inline-block; width: 28px; }
</style>
</head>
<body>
  <section class="card">
    <div class="brand">
      <span class="brand-dot"></span>
      <span class="brand-name">Tidewell Branch Systems Ltd.</span>
    </div>

    <div class="rule rule-top"></div>

    <div class="contact">
      <p class="contact-name">Marlene Voskin</p>
      <p class="contact-role">PT&nbsp;&nbsp;|&nbsp;&nbsp;NV Medicaid Provider</p>
      <p class="contact-line">Phone: (775) 918-2246<span class="gap"></span>Toll-free phone: (877) 461-5092</p>
      <p class="contact-line">Email: mar@tidewellbranchsystemsltd.example</p>
    </div>

    <div class="rule rule-bottom"></div>
  </section>
</body>
</html>
```